Business Card Design for a Personal Trainer

I need a business card design for my job as a personal trainer. It should have a unique, modern and exclusive design. On the front there should be only my logo with my name and my job. 0163/2918374 Tobias Hellwig Lindenkopfweg 14 80921 Munich Germany The most important contact information is the web adress. it can be bigger than the rest, but its not necessary. The card should be 8,5cmx5,5cm big. Font: Roboto. Colors: black, white, gray, 56c1ff.

```html
<!DOCTYPE html>
<html lang="de">
<head>
<meta charset="utf-8">
<title>Tobias Hellwig – Personal Trainer – Visitenkarte</title>
<link href="https://fonts.googleapis.com/css2?family=Roboto:wght@400;500;700&display=swap" rel="stylesheet">
<style>
  :root {
    --backdrop: #8d8d8d;
    --card: #2b2a2b;
    --white: #ffffff;
    --accent: #56c1ff;
    --highlight: #8a8a8a;
    --photo-light: #6a6a6a;
    --photo-dark: #2b2a2b;
  }
  * { margin: 0; padding: 0; box-sizing: border-box; }
  html, body {
    width: 1200px;
    height: 1200px;
    overflow: hidden;
    background: var(--backdrop);
    font-family: "Roboto", sans-serif;
    color: var(--white);
  }
  .card {
    position: absolute;
    left: 219px;
    width: 762px;
    height: 492px;
    background: var(--card);
    overflow: hidden;
  }
  .card--front { top: 91px; }
  .card--back { top: 617px; }

  .brand-mark {
    position: absolute;
    left: 336px;
    top: 140px;
    width: 90px;
    height: 90px;
    background: var(--accent);
  }

  .brand {
    position: absolute;
    left: 0;
    right: 0;
    top: 294px;
    text-align: center;
  }
  .brand__name {
    font-size: 66px;
    font-weight: 400;
    line-height: 1;
    letter-spacing: 0.05em;
    text-transform: uppercase;
  }
  .brand__role {
    display: flex;
    align-items: center;
    justify-content: center;
    gap: 4px;
    margin-top: 14px;
    font-size: 20px;
    font-weight: 400;
    line-height: 1;
    letter-spacing: 0.55em;
    text-transform: uppercase;
  }
  .brand__role-text { margin-right: -0.55em; }
  .brand__rule {
    width: 84px;
    height: 2px;
    background: var(--white);
  }

  .portrait {
    position: absolute;
    left: 45px;
    top: 47px;
    width: 256px;
    height: 445px;
    background: radial-gradient(ellipse at 50% 55%, var(--photo-light) 0%, #4a4a4a 45%, var(--photo-dark) 80%);
  }

  .contact {
    position: absolute;
    left: 327px;
    top: 188px;
    list-style: none;
    font-size: 22px;
    font-weight: 400;
    letter-spacing: 0.19em;
    line-height: 38px;
  }
  .contact__web {
    display: inline-block;
    background: var(--highlight);
    font-weight: 700;
    letter-spacing: 0.22em;
    padding: 0 4px;
    line-height: 29px;
    margin-bottom: 6px;
  }
</style>
</head>
<body>
  <section class="card card--front">
    <div class="brand-mark" aria-hidden="true"></div>
    <div class="brand">
      <div class="brand__name">Tobias Hellwig</div>
      <div class="brand__role">
        <span class="brand__rule"></span>
        <span class="brand__role-text">Personal Trainer</span>
        <span class="brand__rule"></span>
      </div>
    </div>
  </section>

  <section class="card card--back">
    <div class="portrait" role="img" aria-label="Schwarz-Weiß-Porträt des Trainers mit verschränkten Armen"></div>
    <ul class="contact">
      <li><span class="contact__web">www.tobiashellwig.de</span></li>
      <li>t.hellwig@postfach.de</li>
      <li>0163/2918374</li>
      <li>Tobias Hellwig</li>
      <li>Lindenkopfweg 14</li>
      <li>80921 München</li>
    </ul>
  </section>
</body>
</html>
```